Square graphic for social media post

I want to create a 1080 x 1080px all-black image for the quote below that I can share on social media. I want the emphasis to be primarily on the quote, secondarily on the portrait, and third (smallest) on the logo. I want the background on the portrait to be edited so it's transparent and just shows the face of the person on a black background (no brick wall visible).

Graphic color: black
Text color: white
Content: "What we went through is going to make the greatest generation of hoteliers our industry has ever seen." << biggest text
Dorian Welk << smaller text
President, Marrowgate Hotels << smaller text
[image of person - use whichever version looks better to you]
[Add Lodging Ledger logo - whichever looks better to you]

This image needs to be readable when sized down much smaller (400x400?) so want the text and portrait to take up most of the space.

I'd like the output both as PNG and original file (preferably Canva). Thanks!

Target Market(s)

Hotel managers

Industry/Entity Type

Hospitality

Font styles to use
Sans Serif

Colors

Designer to choose colors to be used in the design.

Requirements
Must have
• Needs to focus on the quote and the person quoted (the portrait)

```html
<!DOCTYPE html>
<html lang="en">
<head>
<meta charset="utf-8">
<title>Dorian Welk Quote – Lodging Ledger</title>
<link rel="stylesheet" href="https://fonts.googleapis.com/css2?family=Oswald:wght@400;500;600&display=swap">
<style>
  :root {
    --bg: #000000;
    --ink: #ffffff;
    --portrait-light: #8a8a8a;
    --portrait-mid: #3c3c3c;
    --portrait-dark: #0c0c0c;
  }
  html, body {
    margin: 0;
    padding: 0;
    width: 1200px;
    height: 1200px;
    overflow: hidden;
    background: var(--bg);
  }
  .post {
    position: relative;
    width: 1200px;
    height: 1200px;
    background: var(--bg);
    color: var(--ink);
    font-family: "Oswald", "Arial Narrow", sans-serif;
    overflow: hidden;
  }
  .portrait {
    position: absolute;
    left: 790px;
    top: 0;
    width: 410px;
    height: 1200px;
    background:
      radial-gradient(ellipse 70% 38% at 62% 42%, var(--portrait-light) 0%, var(--portrait-mid) 55%, rgba(12,12,12,0) 100%),
      radial-gradient(ellipse 90% 40% at 70% 88%, var(--portrait-mid) 0%, rgba(12,12,12,0) 100%),
      linear-gradient(90deg, var(--bg) 0%, var(--portrait-dark) 30%, var(--portrait-dark) 100%);
  }
  .quote {
    position: absolute;
    left: 75px;
    top: 70px;
    margin: 0;
    font-weight: 500;
    font-size: 116px;
    line-height: 142px;
    letter-spacing: -0.5px;
  }
  .quote-line {
    display: block;
    white-space: nowrap;
  }
  .quote-line--spaced {
    letter-spacing: 9px;
    word-spacing: 10px;
  }
  .attribution {
    position: absolute;
    left: 75px;
    top: 865px;
    display: flex;
    align-items: baseline;
    gap: 26px;
    white-space: nowrap;
  }
  .attribution-name {
    font-weight: 500;
    font-size: 56px;
  }
  .attribution-role {
    font-weight: 500;
    font-size: 30px;
  }
  .publisher {
    position: absolute;
    left: 80px;
    top: 1060px;
    width: 370px;
    display: flex;
    align-items: center;
    justify-content: center;
    gap: 16px;
  }
  .publisher-dot {
    width: 16px;
    height: 16px;
    border-radius: 50%;
    background: var(--ink);
  }
  .publisher-name {
    font-weight: 500;
    font-size: 40px;
    letter-spacing: 6px;
    text-transform: uppercase;
  }
</style>
</head>
<body>
  <main class="post">
    <div class="portrait" role="img" aria-label="Black-and-white portrait of Dorian Welk, head and shoulders on a black background"></div>

    <blockquote class="quote">
      <span class="quote-line">What we went through</span>
      <span class="quote-line">is going to make the</span>
      <span class="quote-line">greatest generation</span>
      <span class="quote-line quote-line--spaced">of hoteliers our</span>
      <span class="quote-line">industry has ever seen.</span>
    </blockquote>

    <div class="attribution">
      <span class="attribution-name">Dorian Welk</span>
      <span class="attribution-role">- President, Marrowgate Hotels</span>
    </div>

    <div class="publisher">
      <span class="publisher-dot"></span>
      <span class="publisher-name">Lodging Ledger</span>
    </div>
  </main>
</body>
</html>
```